Luxury WordPress Website for CORALBASINS

I need a professional WordPress website for Coral Basins. The site should be modern, visually appealing, and user-friendly, reflecting the brand’s luxury and premium identity. It must include a homepage, product/service pages, contact form, and be responsive on both desktop and mobile devices. The design should allow for easy updates and integration of future content, while maintaining a polished and professional look.

Target Market(s)

swimmingpool & spa

Industry/Entity Type

Swimmingpool

Coding

Coded - Design and coding required

Font styles to use
Other font styles liked:
• HaboroSoft

Requirements
Must have
• Exclusive appearance
Nice to have
• • A logo that subtly incorporates water or pool elements. • A color palette that reflects luxury, elegance, and relaxation. • Clean and modern typography that is easy to read across all media. • Iconography or design elements that convey premium quality. • A versatile design that can be adapted for social media, merchandise, and promotional materials. • Optional: A tagline that emphasizes luxury and high-end pool experiences.

```html
<!DOCTYPE html>
<html lang="en">
<head>
<meta charset="utf-8">
<title>Coral Basins — Luxury Pools</title>
<link href="https://fonts.googleapis.com/css2?family=Tinos:wght@400;700&family=Inter:wght@400;500;600;700&display=swap" rel="stylesheet">
<style>
:root{
  --navy:#0b1742;
  --navy-deep:#091235;
  --blue:#1d86d4;
  --blue-dark:#145fa8;
  --ink:#222631;
  --muted:#555b66;
  --white:#ffffff;
  --water-a:#e9f3fb;
  --water-b:#3a7cc0;
}
*{margin:0;padding:0;box-sizing:border-box}
html,body{width:1200px;height:4549px;overflow:hidden}
body{position:relative;background:var(--white);font-family:"Inter",sans-serif;color:var(--ink)}
.abs{position:absolute}
.serif{font-family:"Tinos",serif}
.btn{position:absolute;display:flex;align-items:center;justify-content:center;background:var(--blue);color:var(--white);border-radius:40px;font-family:"Tinos",serif;font-weight:700;letter-spacing:.5px;border:3px solid #5eb3ee}
.photo{position:absolute}

/* hero */
.hero{position:absolute;left:0;top:0;width:1200px;height:630px;background:linear-gradient(180deg,#3b2a4a 0%,#8a3b44 30%,#d8604a 45%,#5a3440 62%,#2e2a33 80%,#4b3b36 100%)}
.hero-curve{position:absolute;left:0;top:530px;width:1200px;height:100px}
.brand-tab{position:absolute;left:109px;top:0;width:200px;height:203px;background:var(--white);border-radius:0 0 60px 60px;display:flex;flex-direction:column;align-items:center;justify-content:center;gap:12px}
.brand-tab .dot{width:44px;height:44px;border-radius:50%;background:var(--blue)}
.brand-name{font-family:"Tinos",serif;font-weight:700;color:var(--navy);font-size:24px;line-height:1.05;text-align:center}
.nav{position:absolute;top:38px;left:374px;display:flex;gap:0;font-family:"Tinos",serif;font-size:15px;color:var(--white)}
.nav span{position:absolute;white-space:nowrap}
.quote-btn{left:997px;top:30px;width:125px;height:42px;font-size:14px}
.hero-title{position:absolute;left:0;top:205px;width:1200px;text-align:center;font-family:"Tinos",serif;font-weight:700;font-size:62px;line-height:76px;color:var(--white);letter-spacing:1px}
.start-btn{left:499px;top:450px;width:202px;height:60px;font-size:20px}
.scroll-cue{position:absolute;left:589px;top:604px;width:22px;height:34px;border-radius:11px;background:#9a9a9a;display:flex;align-items:center;justify-content:center}

/* section titles */
.sec-title{position:absolute;left:0;width:1200px;text-align:center;font-family:"Tinos",serif;font-weight:700;font-size:42px;color:var(--navy);letter-spacing:.5px}
.sec-title b{color:var(--blue)}
.lead{position:absolute;left:150px;width:900px;text-align:center;font-size:15px;line-height:31px;color:var(--ink)}

/* about */
.about-title{position:absolute;left:110px;top:712px;font-family:"Tinos",serif;font-weight:700;font-size:40px;color:var(--navy)}
.about-title b{color:var(--blue)}
.about-left{position:absolute;left:110px;top:770px;width:440px;font-size:15.5px;line-height:27px}
.about-right{position:absolute;left:664px;top:716px;width:425px;font-size:14.5px;line-height:27.3px;color:var(--muted);text-align:justify}
.about-right p+p{margin-top:27px}
.more-btn{left:664px;top:1088px;width:155px;height:56px;font-size:17px}

.water{position:absolute;left:0;width:1200px;background:linear-gradient(180deg,#ffffff 0%,var(--water-a) 25%,var(--water-b) 50%,#9cc4e8 72%,#ffffff 100%)}

/* types */
.type-card{position:absolute;top:1615px;height:367px;border-radius:4px;overflow:hidden}
.type-card .label{position:absolute;left:50%;top:50%;transform:translate(-50%,-50%) rotate(-90deg);white-space:nowrap;color:var(--white);font-weight:700;font-size:21px}
.feature-bar{position:absolute;left:0;bottom:0;width:100%;height:64px;background:var(--navy);display:flex;align-items:center;justify-content:space-between;padding:0 24px;color:var(--white);font-weight:700;font-size:18px}

/* services */
.services-band{position:absolute;left:0;top:2092px;width:1200px;height:308px;background:linear-gradient(120deg,#0f5aa8,#1b78c9 55%,#1163b2)}
.services-band .sec-title,.services-band .lead{color:var(--white)}
.svc-card{position:absolute;top:2318px;width:466px;height:324px;border:3px solid #dfe6ee;border-radius:4px;overflow:hidden;background:var(--navy)}
.svc-card .photo{left:0;top:0;width:100%;height:266px}
.svc-card .cap{position:absolute;left:0;bottom:0;width:100%;height:52px;display:flex;align-items:center;justify-content:center;color:var(--white);font-size:17px;font-weight:500}
.circle-arrow{position:absolute;width:40px;height:40px}

/* projects */
.proj{position:absolute;border-radius:3px}
.view-btn{left:522px;top:3502px;width:156px;height:56px;font-size:18px}

/* reviews */
.reviews{position:absolute;left:0;top:3631px;width:1200px;height:437px;background:var(--navy-deep)}
.reviews .sec-title{color:var(--white)}
.review{position:absolute;top:3804px;width:301px;height:203px;background:var(--white);border-radius:4px;padding:14px 12px}
.review .avatar{position:absolute;left:8px;top:10px;width:64px;height:64px;border-radius:50%;background:linear-gradient(160deg,#c9b5a0,#7f6b5c)}
.review .stars{position:absolute;left:92px;top:12px;color:#f2b21c;font-size:12px;letter-spacing:1px}
.review .who{position:absolute;left:92px;top:28px;font-weight:700;font-size:17px;color:#111}
.review .when{position:absolute;left:92px;top:52px;font-size:9px;color:#666}
.review .mark{position:absolute;right:14px;top:12px;width:22px;height:22px;border-radius:50%;border:3px solid var(--blue)}
.review p{position:absolute;left:12px;top:92px;width:275px;font-size:13px;line-height:26px;color:#333}

/* footer */
.foot-brand{position:absolute;left:138px;top:4121px;width:176px;height:221px;display:flex;flex-direction:column;align-items:center;justify-content:center;gap:18px}
.foot-brand .dot{width:90px;height:90px;border-radius:50%;background:var(--blue)}
.foot-brand .brand-name{font-size:30px}
.foot-col{position:absolute;top:4146px}
.foot-col h4{font-family:"Tinos",serif;font-weight:700;font-size:20px;color:var(--navy);letter-spacing:.5px;margin-bottom:14px}
.foot-col li{list-style:none;font-size:15px;line-height:30px;color:#222}
.foot-rule{position:absolute;left:100px;top:4377px;width:1000px;height:1px;background:#e3e6ea}
.copyright{position:absolute;left:0;top:4416px;width:1200px;text-align:center;font-size:15px;color:#222}
</style>
</head>
<body>

<!-- HERO -->
<div class="hero" role="img" aria-label="Desert pool at sunset with palm trees reflected in the water"></div>
<svg class="hero-curve" viewBox="0 0 1200 100" preserveAspectRatio="none" aria-hidden="true">
  <path d="M0 10 Q600 150 1200 10 L1200 100 L0 100 Z" fill="#ffffff"/>
</svg>
<div class="scroll-cue"><svg width="10" height="18" viewBox="0 0 10 18"><path d="M5 1v15M1 12l4 4 4-4" stroke="#fff" stroke-width="1.6" fill="none"/></svg></div>

<div class="brand-tab"><span class="dot"></span><div class="brand-name">CORAL<br>BASINS</div></div>
<nav class="nav">
  <span style="left:0;font-weight:700">HOME</span>
  <span style="left:94px">ABOUT</span>
  <span style="left:190px">POOLS</span>
  <span style="left:284px">SERVICES</span>
  <span style="left:400px">GALLERY</span>
  <span style="left:514px">MORE ⌄</span>
</nav>
<div class="btn quote-btn">GET A QUOTE</div>
<h1 class="hero-title">EXCEPTIONAL<br>DESIGN. EXTRAORDINARY<br>SERVICE.</h1>
<div class="btn start-btn">GET STARTED</div>

<!-- ABOUT -->
<h2 class="about-title">ABOUT <b>CORAL BASINS</b></h2>
<p class="about-left">Lorem ipsum dolor sit amet, consectetur adipiscing elit, sed do eiusmod tempor incididunt ut labore et dolore magna aliqua.</p>
<div class="photo" style="left:110px;top:882px;width:490px;height:262px;border-radius:6px;background:linear-gradient(180deg,#8fb9d2,#4f97c4 55%,#2f7fb6)" role="img" aria-label="Family laughing and splashing together in a pool"></div>
<div class="about-right">
  <p>Ut enim ad minim veniam, quis nostrud exercitation ullamco laboris nisi ut aliquip ex ea commodo consequat. Duis aute irure dolor in reprehenderit in voluptate velit esse cillum dolore eu fugiat nulla pariatur. Excepteur sint occaecat cupidatat non proident, sunt in culpa qui officia deserunt mollit anim id est laborum.</p>
  <p>Ut enim ad minima veniam, quis nostrum exercitationem ullam corporis suscipit laboriosam, nisi ut aliquid ex ea commodi consequatur? Quis autem vel eum iure reprehenderit qui in ea voluptate velit esse quam nihil molestiae consequatur, vel illum qui dolorem eum fugiat quo voluptas nulla pariatur.</p>
</div>
<div class="btn more-btn">READ MORE</div>

<div class="water" style="top:1200px;height:180px" role="img" aria-label="Splashing water surface"></div>

<!-- TYPES -->
<h2 class="sec-title" style="top:1455px">TYPES OF <b>POOLS</b></h2>
<p class="lead" style="top:1524px">uis aute irure dolor in reprehenderit in voluptate velit esse cillum dolore eu fugiat nulla pariatur. Excepteur sint occaecat cupidatat non proident, sunt in culpa qui officia deserunt mollit anim id est laborum.</p>
<div class="type-card" style="left:111px;width:143px;background:linear-gradient(180deg,#2a3325,#3e4a3c 50%,#5a4a38)" role="img" aria-label="Gunite pool in a garden"><span class="label">GUNITE POOLS</span></div>
<div class="type-card" style="left:273px;width:143px;background:linear-gradient(180deg,#264e66,#2f6f8e 50%,#3b6d7f)" role="img" aria-label="Fiberglass pool water"><span class="label">FIBERGLASS POOLS</span></div>
<div class="type-card" style="left:434px;width:143px;background:linear-gradient(180deg,#3a4248,#5a6870 50%,#7c8a8c)" role="img" aria-label="Spa with water feature"><span class="label">SPAS &amp; WATER FEATURES</span></div>
<div class="type-card" style="left:596px;width:493px;background:linear-gradient(180deg,#3f7fd0,#9bbfde 40%,#6f8a6a 65%,#1f9fd0)" role="img" aria-label="Resort pool surrounded by palm trees">
  <div class="feature-bar"><span>PALM TREE POOLS</span><svg width="24" height="20" viewBox="0 0 24 20"><path d="M2 10h19M14 3l7 7-7 7" stroke="#fff" stroke-width="2.2" fill="none"/></svg></div>
</div>

<!-- SERVICES -->
<div class="services-band">
  <h2 class="sec-title" style="top:80px;color:#fff">OUR SERVICES</h2>
  <p class="lead" style="top:142px;color:#fff">Duis aute irure dolor in reprehenderit in voluptate velit esse cillum dolore eu fugiat nulla pariatur. Excepteur sint occaecat cupidatat non proident, sunt in culpa qui officia deserunt mollit anim id est laborum.</p>
</div>
<div class="svc-card" style="left:124px">
  <div class="photo" style="background:linear-gradient(180deg,#8e9a8c,#5f7a4d 40%,#2f8bd8 70%,#c9c4bb)" role="img" aria-label="Curved pool with decorative concrete deck"></div>
  <div class="cap">DECORATIVE CONCRETE</div>
</div>
<div class="svc-card" style="left:611px">
  <div class="photo" style="background:linear-gradient(160deg,#0f4c86,#2b8ccf 45%,#5fc0e8 70%,#1a6aa8)" role="img" aria-label="Automatic pool cover rolling over water"></div>
  <div class="cap">AUTOMATIC COVERS</div>
</div>
<svg class="circle-arrow" style="left:38px;top:2460px" viewBox="0 0 40 40"><circle cx="20" cy="20" r="17" fill="none" stroke="#0b1742" stroke-width="2.5"/><path d="M28 20H12M18 14l-6 6 6 6" stroke="#0b1742" stroke-width="2.5" fill="none"/></svg>
<svg class="circle-arrow" style="left:1117px;top:2460px" viewBox="0 0 40 40"><circle cx="20" cy="20" r="17" fill="none" stroke="#0b1742" stroke-width="2.5"/><path d="M12 20h16M22 14l6 6-6 6" stroke="#0b1742" stroke-width="2.5" fill="none"/></svg>

<div class="water" style="top:2670px;height:180px" role="img" aria-label="Splashing water surface"></div>

<!-- PROJECTS -->
<h2 class="sec-title" style="top:2900px">PAST <b>PROJECTS</b></h2>
<div class="proj" style="left:111px;top:2995px;width:272px;height:258px;background:linear-gradient(160deg,#c8b39a,#6aa7cc 60%,#4c8fc0)" role="img" aria-label="Mother and child relaxing by a pool"></div>
<div class="proj" style="left:111px;top:3262px;width:272px;height:187px;background:linear-gradient(180deg,#7b6a58,#5a4a3c)" role="img" aria-label="Crew excavating a pool site"></div>
<div class="proj" style="left:392px;top:2995px;width:399px;height:454px;background:linear-gradient(180deg,#3b8ed6,#6aa25a 45%,#3fb0e2 75%,#8fd3ee)" role="img" aria-label="Children playing with floats in a backyard pool"></div>
<div class="proj" style="left:800px;top:2995px;width:289px;height:186px;background:linear-gradient(180deg,#5e6f8a,#3a4a3c 60%,#2a5f8a)" role="img" aria-label="Lit pool at dusk"></div>
<div class="proj" style="left:800px;top:3189px;width:289px;height:260px;background:linear-gradient(180deg,#6b4a7a,#c76a7a 35%,#5f7f4c 60%,#3f9ad0 80%,#a9a8a2)" role="img" aria-label="Rectangular pool under a pink sunset"></div>
<div class="btn view-btn">VIEW MORE</div>

<!-- REVIEWS -->
<div class="reviews">
  <h2 class="sec-title" style="top:90px;color:#fff">WHAT OUR <b>CUSTOMER SAYS</b></h2>
</div>
<div class="review" style="left:111px"><span class="avatar" role="img" aria-label="Customer portrait"></span><span class="stars">★★★★★</span><span class="who">Evan Hale</span><span class="when">3 days ago</span><span class="mark"></span><p>Great company for all your pool needs, small or large they can take care of it.</p></div>
<div class="review" style="left:448px"><span class="avatar" role="img" aria-label="Customer portrait"></span><span class="stars">★★★★★</span><span class="who">Marcus Reed</span><span class="when">6 days ago</span><span class="mark"></span><p>Absolutely hands-down, the best pool service company in Ohio. Everybody at Lakeside pool company are truly professi -onals and treat all of us like family!</p></div>
<div class="review" style="left:787px"><span class="avatar" role="img" aria-label="Customer portrait"></span><span class="stars">★★★★★</span><span class="who">Peter Lane</span><span class="when">25 days ago</span><span class="mark"></span><p>I have used Coral Basins for years. They are the absolute best! The techs know what they are doing, prompt and efficient.</p></div>
<svg class="circle-arrow" style="left:38px;top:3886px" viewBox="0 0 40 40"><circle cx="20" cy="20" r="17" fill="none" stroke="#fff" stroke-width="2.5"/><path d="M28 20H12M18 14l-6 6 6 6" stroke="#fff" stroke-width="2.5" fill="none"/></svg>
<svg class="circle-arrow" style="left:1115px;top:3886px" viewBox="0 0 40 40"><circle cx="20" cy="20" r="17" fill="none" stroke="#fff" stroke-width="2.5"/><path d="M12 20h16M22 14l6 6-6 6" stroke="#fff" stroke-width="2.5" fill="none"/></svg>

<!-- FOOTER -->
<div class="foot-brand"><span class="dot"></span><div class="brand-name">CORAL<br>BASINS</div></div>
<div class="foot-col" style="left:392px"><h4>QUICK LINKS</h4><ul><li>Home</li><li>About Us</li><li>Services</li><li>Types of Pool</li><li>Contact Us</li></ul></div>
<div class="foot-col" style="left:598px"><h4>HELP LINKS</h4><ul><li>FAQ</li><li>Term of Use</li><li>Privacy Policy</li><li>Terms &amp; Conditions</li><li>Support Links</li></ul></div>
<div class="foot-col" style="left:821px"><h4>CONTACT US</h4><ul><li>Location: Coral Basins</li><li>United States</li><li>Email Us: info@coralbasins.com</li><li>Phone: +1 555 010 2040</li></ul></div>
<div class="foot-rule"></div>
<p class="copyright">Copyrights@2025.Coral Basins.All Rights Reserved</p>
<div class="water" style="top:4460px;height:89px;background:linear-gradient(180deg,#ffffff 0%,#9cc4e8 45%,#3a7cc0 100%)" role="img" aria-label="Splashing water surface"></div>

</body>
</html>
```